label design for oral care product

Kindly invite you to design bottle label (114 mm*40 mm) for our product, a kind of oral care product. The GEL is different from our previous cleanser product, as the pic we uploaded for demonstration. The color of frosted glass bottle is dark green, but the cap is white. You could download the pic of bottle among the uploaded files. The logo file and label content description are attached too. Please check them. Our product is made from many kinds of natural plant extracts, which includes herb and fruit. I wish the label would make our product look high-end and reliable. And it would be better if you could give some advice on paper material and special requirements for printing, related to your design. I value the texture of label too, because I think that stands for the quality of products. No color limitation for the use of our logo.
20-40 female, who value oral health.

```html
<!DOCTYPE html>
<html lang="en">
<head>
<meta charset="utf-8">
<title>Sprig Mist Aligner Gel — Bottle Label</title>
<link href="https://fonts.googleapis.com/css2?family=Bree+Serif&family=Roboto:ital,wght@0,400;0,700;0,900;1,700&display=swap" rel="stylesheet">
<style>
  :root {
    --stage: #3a3a3c;
    --ink: #161616;
    --white: #ffffff;
    --blue-deep: #2f5fc0;
    --blue-mid: #1f9fe4;
    --blue-bright: #27c3ee;
    --blue-pale: #8fd6f0;
    --band-blue: #2c8fe0;
    --panel: rgba(190, 235, 250, 0.38);
  }
  * { box-sizing: border-box; margin: 0; padding: 0; }
  html, body { width: 1200px; height: 554px; overflow: hidden; background: var(--stage); }
  .canvas { position: relative; width: 1200px; height: 554px; }

  .label {
    position: absolute; left: 103px; top: 103px; width: 994px; height: 349px;
    border-radius: 44px; overflow: hidden;
    background: linear-gradient(90deg, var(--blue-pale) 0%, var(--blue-mid) 30%, var(--blue-deep) 50%, var(--blue-mid) 70%, var(--blue-pale) 100%);
    box-shadow: 8px 14px 22px rgba(0,0,0,0.45);
    font-family: "Roboto", Arial, sans-serif; color: var(--ink);
  }
  .label__backdrop { position: absolute; inset: 0; width: 100%; height: 100%; }

  .info-panel {
    position: absolute; top: 26px; width: 279px; height: 296px;
    border-radius: 20px; background: var(--panel);
    text-align: center; font-size: 17.4px; line-height: 22px;
  }
  .info-panel--contains { left: 20px; padding: 34px 14px 0; }
  .info-panel--directions { left: 698px; padding: 20px 12px 0; }
  .info-panel__title { font-weight: 700; font-size: 17.4px; }
  .info-panel__blank {
    position: absolute; left: 45px; top: 189px; width: 189px; height: 89px; background: var(--white);
  }

  .brand {
    position: absolute; left: 397px; top: 52px; width: 200px;
    display: flex; align-items: center; justify-content: center; gap: 6px;
    font-weight: 900; font-size: 34px; line-height: 1; color: var(--ink); letter-spacing: -0.5px;
  }
  .brand__dot { width: 12px; height: 12px; border-radius: 50%; background: var(--ink); }

  .product-name {
    position: absolute; left: 297px; top: 140px; width: 400px; text-align: center;
    font-family: "Bree Serif", Georgia, serif; font-size: 56px; line-height: 1;
    color: var(--white); -webkit-text-stroke: 12px var(--ink); paint-order: stroke fill;
  }
  .claim-band {
    position: absolute; left: 347px; top: 195px; width: 300px; height: 46px; z-index: -0;
  }
  .claim-band__text {
    position: absolute; left: 347px; top: 213px; width: 300px; text-align: center;
    color: var(--white); font-weight: 700; font-style: italic; font-size: 17px;
  }
  .product-name { z-index: 2; }
  .claim-band, .claim-band__text { z-index: 1; }

  .benefit {
    position: absolute; left: 347px; top: 248px; width: 300px; text-align: center;
    font-weight: 700; font-style: italic; font-size: 18px; line-height: 20px; color: #2a2a2a;
  }
  .volume {
    position: absolute; left: 427px; top: 312px; width: 139px; height: 40px;
    border-radius: 20px 20px 0 0;
    background: linear-gradient(180deg, #bfe8f7 0%, #8fd0f0 100%);
    text-align: center; font-weight: 700; font-size: 15px; line-height: 30px; color: #2a2a2a;
  }
</style>
</head>
<body>
<div class="canvas">
  <div class="label">
    <svg class="label__backdrop" viewBox="0 0 994 349" aria-hidden="true">
      <ellipse cx="497" cy="360" rx="470" ry="330" fill="none" stroke="rgba(170,230,250,0.45)" stroke-width="40"/>
      <ellipse cx="497" cy="380" rx="380" ry="300" fill="rgba(60,200,240,0.35)"/>
      <path d="M170 0 L270 349 L200 349 Z" fill="rgba(150,215,245,0.35)"/>
      <path d="M824 0 L724 349 L794 349 Z" fill="rgba(150,215,245,0.35)"/>
      <path d="M497 12 C430 60 330 170 292 243 C330 290 370 330 396 349 L598 349 C624 330 664 290 702 243 C664 170 564 60 497 12 Z" fill="#ffffff"/>
      <path class="claim-shape" d="M355 197 L639 197 L625 232 Q620 242 608 242 L386 242 Q374 242 369 232 Z" fill="#2c8fe0"/>
    </svg>

    <div class="info-panel info-panel--contains">
      <p class="info-panel__title">CONTAINS:</p>
      <p>a proprietary blend of natural plant extract including Angelica, Radix Rehmanniae, Coptis, Honeysuckle, Echinacea, Sage, Chamomile, Acerola cherry.</p>
    </div>

    <div class="brand"><span>Sprig Mist</span><span class="brand__dot"></span></div>
    <h1 class="product-name">Aligner Gel</h1>
    <p class="claim-band__text">Immune Support for Oral Health</p>
    <p class="benefit">Solution to Maintain Dental<br>Hygiene and Strengthen Gums</p>
    <div class="volume">30 ml / 1 fl oz</div>

    <div class="info-panel info-panel--directions">
      <p class="info-panel__title">DIRECTIONS:</p>
      <p>Drop on the teeth directly after brushing. Or, put into clear aligners before wearing again. No need to rinse your mouth with water.</p>
      <div class="info-panel__blank"></div>
    </div>
  </div>
</div>
</body>
</html>
```